Business Card Design

Online clothing womens clothing store, I sell my clothing online and at the markets.

i would like the attached picture on the front of the card and the contact information on the back.

Industry/Entity Type

Business

Contact Information for Business Card

Velvet Harbour
Marnie Talbot
(Instagram symbol) _velvet_harbour_
(Facebook symbol) www.facepage-example.com/velvetharbourau/

W : www.velvetharbour-example.com.au
E : info@velvetharbour-example.com.au
P : 0491876324

```html
<!DOCTYPE html>
<html lang="en">
<head>
<meta charset="utf-8">
<title>Velvet Harbour – Business Card</title>
<link rel="stylesheet" href="https://fonts.googleapis.com/css2?family=Lato:wght@300;400;700;900&display=swap">
<style>
  :root {
    --stage: #2a2a2a;
    --paper: #f4f4f4;
    --paper-shade: #e2e2e2;
    --ink: #0b0b0b;
    --muted: #8a8a8a;
    --muted-dark: #5f5f5f;
    --rule: #bdbdbd;
    --white: #ffffff;
    --light: #e8e8e8;
  }
  * { box-sizing: border-box; margin: 0; padding: 0; }
  html, body {
    width: 1200px; height: 997px; overflow: hidden;
    background: var(--stage);
    font-family: "Lato", sans-serif;
  }
  .stage {
    width: 1200px; height: 997px;
    display: flex; flex-direction: column; align-items: center; justify-content: center;
    gap: 40px;
  }
  .card {
    position: relative;
    width: 760px; height: 434px;
    overflow: hidden;
    box-shadow: 0 12px 30px rgba(0,0,0,.5);
  }

  /* Front */
  .card-front__photo {
    position: absolute; inset: 0;
    background:
      radial-gradient(ellipse at 62% 30%, #3f4a4e 0%, #2c3437 30%, transparent 60%),
      linear-gradient(125deg, #c9d3d6 0%, #dfe5e6 30%, #9fb3b6 55%, #56696c 75%, #3b4649 100%);
  }
  .card-front__name {
    position: absolute; right: 46px; bottom: 60px;
    font-weight: 900; font-size: 72px; letter-spacing: 3px;
    color: var(--white); text-transform: uppercase;
  }

  /* Back */
  .card-back { background: linear-gradient(180deg, var(--paper), var(--paper-shade)); }
  .card-back__brand {
    position: absolute; top: 40px; left: 0; right: 0;
    text-align: center;
    font-weight: 300; font-size: 30px; letter-spacing: 9px;
    color: var(--ink); text-transform: uppercase;
  }
  .card-back__band {
    position: absolute; left: 0; right: 0; top: 110px; height: 250px;
    background: var(--ink);
    color: var(--white);
  }
  .rule { position: absolute; height: 2px; background: var(--rule); }
  .person {
    position: absolute; top: 20px; left: 0; right: 0; text-align: center;
  }
  .person__name { font-weight: 900; font-size: 24px; line-height: 30px; letter-spacing: .5px; text-transform: uppercase; }
  .person__role { margin-top: 2px; font-weight: 400; font-size: 16px; color: var(--muted); }
  .rule--role-right { top: 44px; left: 500px; right: 28px; }
  .rule--role-left { top: 64px; left: 210px; width: 130px; }
  .rule--split { top: 110px; left: 28px; width: 310px; }
  .contact {
    position: absolute; list-style: none;
    font-size: 17px; font-weight: 400; color: var(--light);
  }
  .contact li { display: flex; align-items: center; gap: 12px; height: 32px; white-space: nowrap; }
  .contact svg { flex: none; }
  .contact--social { left: 420px; top: 92px; font-size: 16px; }
  .contact--direct { left: 30px; top: 160px; }
  .social-mark { width: 16px; height: 16px; background: var(--light); border-radius: 3px; flex: none; }
  .card-back__web {
    position: absolute; bottom: 30px; left: 0; right: 0; text-align: center;
    font-size: 17px; letter-spacing: 6px; color: var(--muted-dark);
  }
</style>
</head>
<body>
<main class="stage">
  <section class="card card-front">
    <div class="card-front__photo" role="img" aria-label="Photograph of a woman with dark windswept hair against a pale misty sky"></div>
    <p class="card-front__name">Velvet Harbour</p>
  </section>

  <section class="card card-back">
    <h1 class="card-back__brand">Velvet Harbour</h1>
    <div class="card-back__band">
      <div class="person">
        <p class="person__name">Marnie Talbot</p>
        <p class="person__role">Owner</p>
      </div>
      <span class="rule rule--role-right"></span>
      <span class="rule rule--role-left"></span>
      <span class="rule rule--split"></span>
      <ul class="contact contact--social">
        <li><span class="social-mark"></span>_velvet_harbour_</li>
        <li><span class="social-mark"></span>facepage-example.com/velvetharbour</li>
      </ul>
      <ul class="contact contact--direct">
        <li>
          <svg width="16" height="22" viewBox="0 0 16 22" aria-hidden="true"><rect x="1.5" y="1.5" width="13" height="19" rx="2" fill="none" stroke="#e8e8e8" stroke-width="2"/><line x1="6" y1="17" x2="10" y2="17" stroke="#e8e8e8" stroke-width="1.5"/></svg>
          0491876324
        </li>
        <li>
          <svg width="22" height="16" viewBox="0 0 22 16" aria-hidden="true"><rect x="1" y="1" width="20" height="14" fill="none" stroke="#e8e8e8" stroke-width="2"/><polyline points="1,1 11,9 21,1" fill="none" stroke="#e8e8e8" stroke-width="2"/></svg>
          info@velvetharbour-example.com.au
        </li>
      </ul>
    </div>
    <p class="card-back__web">www.velvetharbour-example.com.au</p>
  </section>
</main>
</body>
</html>
```